redesing professional certificate

Redesign our certificate to more a professional look and to make it look like a-wanna have - Best in adobe photoshop, because this template will be our basic, and we have in our education different levels, basic, upper, lower, complex, master level. I usually add a small picture to show what level they are. Or when you have a better suggestion I a gladly to hear.
We teach to physiotherapist so it has to look professional.

Target Market(s)

physiotherapist

Industry/Entity Type

Health Care

Requirements
Must have
• our logo

```html
<!DOCTYPE html>
<html lang="en">
<head>
<meta charset="utf-8">
<title>Certificate</title>
<link href="https://fonts.googleapis.com/css2?family=Cinzel:wght@500&family=Open+Sans:wght@400;600;700&display=swap" rel="stylesheet">
<style>
  :root{
    --navy:#17214a;
    --navy-deep:#0f1735;
    --gold:#e2b33c;
    --gold-light:#f5d77a;
    --gold-dark:#a87a1c;
    --ink:#2b2f45;
    --paper:#ffffff;
  }
  *{margin:0;padding:0;box-sizing:border-box}
  html,body{width:788px;height:1200px;overflow:hidden;background:var(--paper)}
  body{font-family:"Open Sans",sans-serif;color:var(--ink)}
  .certificate{position:relative;width:788px;height:1200px;background:var(--paper);overflow:hidden}
  .header-band{position:absolute;top:0;left:0;width:788px;height:400px}
  .title{position:absolute;top:78px;left:0;width:100%;text-align:center;
    font-family:"Cinzel",serif;font-weight:500;font-size:64px;letter-spacing:5px;color:var(--gold)}
  .brand-mark{position:absolute;top:258px;left:326px;width:136px;height:136px;border-radius:50%;
    background:var(--gold);display:flex;align-items:center;justify-content:center}
  .brand-name{font-family:"Open Sans",sans-serif;font-weight:700;font-size:40px;color:var(--navy);letter-spacing:2px}
  .recipient{position:absolute;top:422px;width:100%;text-align:center;font-size:44px;font-weight:400;color:var(--navy)}
  .course-details{position:absolute;top:494px;width:100%;text-align:center;font-size:21px;line-height:37px;color:var(--ink)}
  .seal{position:absolute;top:628px;left:300px;width:188px;height:188px}
  .signatory{position:absolute;top:712px;width:240px;text-align:center;font-size:19px;line-height:27px;color:var(--ink)}
  .signatory.left{left:104px}
  .signatory.right{left:444px}
  .signatory strong{display:block;font-weight:700;color:var(--navy)}
  .registration{position:absolute;top:850px;width:100%;text-align:center;font-size:20px;color:var(--ink)}
  .terms{position:absolute;top:900px;left:90px;width:608px;text-align:center;font-size:20px;line-height:31px;color:var(--ink)}
  .footer{position:absolute;left:0;bottom:0;width:788px;height:160px;background:var(--navy);
    border-bottom:10px solid var(--gold)}
  .footer-address{position:absolute;left:30px;top:30px;font-size:16px;line-height:24px;color:#fff}
  .footer-address .company{color:var(--gold)}
  .footer-tagline{position:absolute;right:24px;top:30px;width:190px;padding:10px 16px;
    border:2px solid var(--gold);border-left-width:5px;background:#fff;font-size:16px;line-height:22px;color:var(--navy)}
  .footer-tagline .accent{color:var(--gold-dark)}
</style>
</head>
<body>
<main class="certificate">
  <svg class="header-band" viewBox="0 0 788 400" role="img" aria-label="Navy header band with fine geometric line pattern and gold edge">
    <defs>
      <linearGradient id="bandFill" x1="0" y1="0" x2="1" y2="1">
        <stop offset="0" stop-color="#1c2756"/>
        <stop offset="1" stop-color="#0f1735"/>
      </linearGradient>
    </defs>
    <polygon points="0,0 788,0 788,248 394,372 0,248" fill="url(#bandFill)"/>
    <polyline points="0,262 394,388 788,262" fill="none" stroke="#e2b33c" stroke-width="6"/>
  </svg>

  <h1 class="title">Certificate</h1>

  <div class="brand-mark"><span class="brand-name">MBT</span></div>

  <p class="recipient">Lena Marquardt</p>

  <p class="course-details">
    has completed the fasciatherapy level I course<br>
    - 3 days, 75-77 february 2020 -<br>
    Kópavogur, Iceland 77 february 2020.
  </p>

  <svg class="seal" viewBox="0 0 188 188" role="img" aria-label="Gold certification seal">
    <defs>
      <radialGradient id="sealFill" cx="0.4" cy="0.35" r="0.7">
        <stop offset="0" stop-color="#f7dc86"/>
        <stop offset="0.6" stop-color="#d9a733"/>
        <stop offset="1" stop-color="#9c6f17"/>
      </radialGradient>
    </defs>
    <circle cx="94" cy="94" r="90" fill="url(#sealFill)"/>
    <circle cx="94" cy="94" r="72" fill="none" stroke="#a87a1c" stroke-width="3"/>
  </svg>

  <div class="signatory left">Mr. J.P. van Loon<strong>Co-Director</strong></div>
  <div class="signatory right">Mr. T.R. Halberg<strong>Co-Director</strong></div>

  <p class="registration">Registration number: 7 ICE 20</p>

  <p class="terms">The Myofascial Balance Therapy ongoing certification is contingent upon meeting the requirements of the maintenance of the certification of Fasciatherapy</p>

  <footer class="footer">
    <p class="footer-address">
      <span class="company">Fasciora BV</span><br>
      Keizerslaan 14, 1021AB Amsterdam<br>
      The Netherlands
    </p>
    <p class="footer-tagline">Specialists in <span class="accent">fasciatherapy innovation</span></p>
  </footer>
</main>
</body>
</html>
```